High End Business Card Design for Flooring Store

Looking for a new card design for our hardwood flooring company. We have no print budget for these and are open to cards made from wood, metal, cardstock with embossed print ... or any combination of these. No plastic.

We sell luxury products and I want the cards to reflect our image of quality and class.

Our contact information as such;
Employee Name
248 Halloway Blvd.
Dieppe, NB
E3C-4K9
(506) 555-0142
Employee email @kestraflooring.com

Target Market(s)

Home Builders

Contact Information for Business Card

Emnployee name, business contact information

```html
<!DOCTYPE html>
<html lang="en">
<head>
<meta charset="utf-8">
<title>Kestra Flooring – Business Card</title>
<link rel="stylesheet" href="https://fonts.googleapis.com/css2?family=Montserrat:wght@400;500&family=Arimo:wght@400;700&display=swap">
<style>
  :root {
    --backdrop: #e3e3e3;
    --card-white: #f5f5f6;
    --brand-red: #862523;
    --brand-gold: #d9a321;
    --tagline-grey: #6a6a6a;
    --ink: #1c1c1c;
    --rule: #2a2a2a;
    --white: #ffffff;
  }
  * { margin: 0; padding: 0; box-sizing: border-box; }
  html, body { width: 1200px; height: 1040px; overflow: hidden; }
  body { background: var(--backdrop); position: relative; font-family: "Arimo", Arial, sans-serif; }

  .card {
    position: absolute;
    left: 284px;
    width: 642px;
    height: 366px;
    border-radius: 18px;
  }
  .card--front { top: 130px; background: var(--card-white); }
  .card--back { top: 568px; background: var(--brand-red); }

  /* Brand wordmark */
  .brand {
    position: absolute;
    display: flex;
    align-items: center;
    font-family: "Montserrat", sans-serif;
    font-weight: 500;
    line-height: 1;
  }
  .brand__square { display: block; background: var(--brand-gold); }
  .brand--front { right: 42px; top: 46px; color: var(--brand-red); font-size: 56px; gap: 10px; }
  .brand--front .brand__square { width: 34px; height: 34px; }
  .brand--back { left: 0; right: 0; justify-content: center; top: 114px; color: var(--white); font-size: 90px; gap: 16px; }
  .brand--back .brand__square { width: 52px; height: 52px; }

  .tagline {
    position: absolute;
    text-align: center;
    font-family: "Montserrat", sans-serif;
    font-weight: 400;
  }
  .tagline--front { right: 78px; top: 96px; color: var(--tagline-grey); font-size: 16px; line-height: 17px; }
  .tagline--back { left: 0; right: 0; top: 198px; color: var(--white); font-size: 24px; line-height: 26px; font-weight: 500; }

  /* Person */
  .person { position: absolute; left: 45px; top: 209px; }
  .person__name { color: var(--brand-red); font-weight: 700; font-size: 25px; line-height: 28px; }
  .person__title { color: var(--brand-gold); font-size: 16px; line-height: 19px; margin-left: 2px; }

  .divider { position: absolute; left: 45px; right: 44px; top: 263px; height: 1px; background: var(--rule); }

  .contact-list { position: absolute; left: 45px; top: 274px; list-style: none; }
  .contact-list li {
    display: flex; align-items: center; gap: 8px;
    color: var(--ink); font-size: 16.5px; line-height: 20px;
  }
  .contact-list svg { width: 14px; height: 14px; fill: var(--brand-red); flex: none; }

  .address {
    position: absolute; right: 44px; top: 274px;
    text-align: right; font-style: normal;
    color: var(--ink); font-size: 16.5px; line-height: 20px;
  }

  .web-url {
    position: absolute; left: 0; right: 0; top: 322px;
    text-align: center; color: var(--white);
    font-size: 16px; letter-spacing: 4.2px;
  }
</style>
</head>
<body>

<section class="card card--front" aria-label="Business card front">
  <div class="brand brand--front"><span class="brand__square"></span>Kestra</div>
  <p class="tagline tagline--front">Planchers &amp; Escaliers<br>Flooring &amp; Stairs</p>

  <div class="person">
    <h1 class="person__name">Daniel Arsenault</h1>
    <p class="person__title">President</p>
  </div>

  <div class="divider"></div>

  <ul class="contact-list">
    <li>
      <svg viewBox="0 0 14 14" aria-hidden="true"><path d="M3.5 0h7a1 1 0 0 1 1 1v12a1 1 0 0 1-1 1h-7a1 1 0 0 1-1-1V1a1 1 0 0 1 1-1zm.8 1.6v9.2h5.4V1.6zM7 11.6a.8.8 0 1 0 0 1.6.8.8 0 0 0 0-1.6z"/></svg>
      (506) 555-0142
    </li>
    <li>
      <svg viewBox="0 0 14 14" aria-hidden="true"><path d="M0 3h14v9H0zm1.4 1.2L7 8.2l5.6-4z"/></svg>
      danielarsenault@kestraflooring.com
    </li>
    <li>
      <svg viewBox="0 0 14 14" aria-hidden="true"><path d="M7 0a7 7 0 1 0 0 14A7 7 0 0 0 7 0zm-2 2.2c.6.9.4 1.6-.4 2.1-.9.5-1 1.4-.2 2 .9.6 1.8.2 2.3 1.1.4.8-.3 1.9.3 2.7.5.7 1.3.4 1.8 1.3-2.9.9-6.4-1.2-6.5-4.4 0-2 1.1-3.9 2.7-4.8zm4.6.4c1.7 1 2.9 3.2 2.3 5.4-.7-.4-1.2-1.3-2.1-1.2-.9.1-1.5-.7-1.2-1.6.3-.9 1.2-1.1 1-2.6z"/></svg>
      www.kestraflooring.com
    </li>
  </ul>

  <address class="address">
    248 Halloway Blvd.<br>
    Dieppe, NB<br>
    E3C-4K9
  </address>
</section>

<section class="card card--back" aria-label="Business card back">
  <div class="brand brand--back"><span class="brand__square"></span>Kestra</div>
  <p class="tagline tagline--back">Planchers &amp; Escaliers<br>Flooring &amp; Stairs</p>
  <p class="web-url">www.kestraflooring.com</p>
</section>

</body>
</html>
```